(Wix) Website Design Tweaks

The site: www.MarbleFinchCo.com
(The coding must be done within Wix. I will create a duplicate website so you can gain access and begin editing.)

My website contains my preferred text and images - but it needs to look more professional. My business focuses on "Corporate Messaging" and "Marketing Communications", so the website needs to look professional, but not too corporate. My clients range from very big companies to technology startups - the look and feel should be uncluttered, professional, and modern.

I want someone to review the pages, and make changes / suggestions focused on:
1) Fonts
2) Colors
3) Layout

If you have ideas for adding additional graphics, that's fine, but they should be consistent with what I already have . . . unless you think some / all of my images need to be changed.

My site is very, very small, and only contains 5 (very short) pages. There are no sub-pages. (One page is the contact page, with almost nothing except form fields.)

If you do a good job with my site, I may be able to provide you with additional work - many of my clients need website design tweaks, after I provide the verbiage.

```html
<!DOCTYPE html>
<html lang="en">
<head>
<meta charset="utf-8">
<title>Marble Finch Co — Inform. Influence. Sell</title>
<link href="https://fonts.googleapis.com/css2?family=Montserrat:ital,wght@0,300;0,400;0,500;0,600;0,700;1,400&display=swap" rel="stylesheet">
<style>
:root{
  --blue:#0ba6ee;
  --blue-dark:#0a8fd0;
  --tint:#eef4fc;
  --ink:#1e1e24;
  --body:#3a3a44;
  --muted:#8c8f99;
  --line:#e3e7ee;
  --dark:#1c1c1f;
  --darker:#141416;
  --white:#ffffff;
}
*{box-sizing:border-box;margin:0;padding:0}
html,body{width:1200px;height:4187px;overflow:hidden}
body{position:relative;font-family:'Montserrat',sans-serif;color:var(--ink);background:var(--white)}
.abs{position:absolute}
.band{position:absolute;left:0;width:1200px}
.art{position:absolute;border-radius:6px}
.art-blue{background:linear-gradient(135deg,#d7ebfb 0%,#a9d8f7 55%,#5bbdf1 100%)}
.art-soft{background:linear-gradient(135deg,#f3f6fa 0%,#dde9f6 60%,#bfe0f7 100%)}
.btn{position:absolute;display:flex;align-items:center;justify-content:center;font-size:12px;font-weight:600;border-radius:4px 4px 14px 4px}
.btn-fill{background:var(--blue);color:var(--white)}
.btn-line{border:1.5px solid var(--blue);color:var(--blue);background:var(--white)}
.eyebrow{position:absolute;font-size:11.5px;color:var(--blue);text-transform:uppercase;letter-spacing:.2px}
.heading{position:absolute;font-size:29px;font-weight:400;line-height:36px;color:var(--ink);white-space:nowrap}
.heading b{font-weight:700}
.copy{position:absolute;font-size:11.5px;line-height:22.6px;color:var(--body)}

/* header */
.logo-box{left:159px;top:20px;width:101px;height:99px;background:var(--blue);color:var(--white);font-size:17px;line-height:20px;padding:50px 0 0 8px;font-weight:400}
.nav{left:0;top:61px;font-size:12.5px;color:var(--body)}
.nav span{position:absolute;white-space:nowrap}
.hero-title{left:0;top:174px;width:1200px;text-align:center;font-size:45px;font-weight:300;letter-spacing:1px}
.hero-title b{font-weight:700}
.hero-copy{left:300px;top:244px;width:600px;text-align:center;font-size:12px;line-height:19px;color:var(--body)}

/* logo strip */
.brands{top:715px;height:111px;background:var(--white);border-bottom:1px solid var(--line)}
.brand{position:absolute;top:44px;font-size:15px;font-weight:600;color:#a7abb3;white-space:nowrap;transform:translateX(-50%)}

/* services */
.cell{position:absolute;border-color:var(--line);border-style:solid;border-width:0}
.cell .art{left:36px;right:36px}
.cell-label{position:absolute;left:0;right:0;text-align:center;font-size:14.5px;line-height:18px;color:var(--ink)}

/* testimonials */
.quote{position:absolute;background:var(--white);box-shadow:0 2px 8px rgba(20,40,80,.06);padding:0 20px 0 22px}
.quote p{font-size:12.5px;font-style:italic;line-height:20px;color:var(--body)}
.quote h4{font-size:14px;font-weight:700;margin-top:18px;color:var(--ink)}
.quote small{display:block;font-size:9.5px;line-height:11px;color:var(--body)}
.quote-mark{position:absolute;top:-22px;right:20px;font-size:86px;line-height:86px;font-weight:700;color:var(--blue);font-family:'Montserrat',sans-serif}

/* community */
.community{left:192px;top:3585px;width:816px;height:239px;background:var(--blue);border-radius:60px 80px 4px 60px;color:var(--white)}
.field{position:absolute;top:152px;height:40px;background:var(--white);border-radius:4px 4px 14px 4px;color:#8a8f99;font-size:12.5px;padding:12px 18px}

/* footer */
.footer{top:3655px;height:532px;background:var(--dark)}
.footer-bar{top:4114px;height:73px;background:var(--darker)}
.ft{position:absolute;color:#d6d8dd;font-size:11.5px;line-height:26px}
.ft-h{position:absolute;color:var(--white);font-size:15px;font-weight:600}
</style>
</head>
<body>

<div class="band" style="top:0;height:715px;background:var(--tint)"></div>
<svg class="abs" style="left:1040px;top:50px" width="160" height="260" aria-hidden="true">
  <circle cx="160" cy="130" r="128" fill="none" stroke="#7fc8f3" stroke-width="1.5" stroke-dasharray="5 6"/>
</svg>

<header>
  <div class="abs logo-box">MARBLE<br>FINCH CO</div>
  <nav class="abs nav">
    <span style="left:384px">Home</span>
    <span style="left:463px">FinchCamp</span>
    <span style="left:574px">Testimonials</span>
    <span style="left:691px">Team</span>
    <span style="left:766px">Contact</span>
  </nav>
  <div class="btn btn-fill" style="left:909px;top:50px;width:130px;height:38px">Join Us</div>
</header>

<section class="hero">
  <h1 class="abs hero-title">INFORM . <b>INFLUENCE</b> . SELL</h1>
  <p class="abs hero-copy">Lorem ipsum dolor sit amet, consectetur adipisicing elit, sed do eiusmod tempor incididunt ut labore et dolore magna aliqua.</p>
  <div class="btn btn-fill" style="left:460px;top:306px;width:130px;height:40px">Learn More</div>
  <div class="btn btn-line" style="left:608px;top:306px;width:130px;height:40px">Contact us</div>
  <div class="art art-blue" role="img" aria-label="Illustration of people promoting messages across phones, laptops and social media around a globe" style="left:60px;top:355px;width:1110px;height:360px;border-radius:8px 8px 0 0"></div>
</section>

<section class="band brands" aria-label="Clients">
  <span class="brand" style="left:192px">Northgate</span>
  <span class="brand" style="left:309px">Orchard</span>
  <span class="brand" style="left:424px">Telvia</span>
  <span class="brand" style="left:540px">Indigo Stage</span>
  <span class="brand" style="left:659px">Crestline</span>
  <span class="brand" style="left:776px">Netwave</span>
  <span class="brand" style="left:893px">Cityvault</span>
  <span class="brand" style="left:1009px">Fizzara</span>
</section>

<section class="challenge">
  <span class="eyebrow" style="left:159px;top:934px">The big challenge</span>
  <h2 class="heading" style="left:159px;top:962px">Why you need to have a <b>good</b><br><b>Communication</b> skills?</h2>
  <p class="copy" style="left:159px;top:1062px;width:436px">In today's competitive business environment, effective communication is more essential than ever before. It is the foundation upon which companies are built, careers are propelled, and knowledge is imparted. Effective communication is critical - without it, misunderstandings arise, errors occur, and business goals are frustrated. In short, effective communication is the key driver of long-term business and professional success.</p>
  <div class="btn btn-fill" style="left:159px;top:1228px;width:131px;height:39px">Learn More</div>
  <div class="art art-soft" role="img" aria-label="Illustration of business people presenting a growing bar chart" style="left:642px;top:967px;width:431px;height:301px"></div>
</section>

<section class="help">
  <div class="art art-soft" role="img" aria-label="Illustration of a team launching a rocket toward a target" style="left:138px;top:1366px;width:407px;height:260px"></div>
  <span class="eyebrow" style="left:603px;top:1375px">Grow with us</span>
  <h2 class="heading" style="left:603px;top:1404px">How we <b>help?</b></h2>
  <p class="copy" style="left:603px;top:1464px;width:410px">At Marble Finch Co, we help individuals and organizations "get what they want" through clear and persuasive communication. Our consulting, coaching, and training services help clients achieve targeted business objectives, with an emphasis on informing, influencing, and selling.</p>
  <div class="btn btn-fill" style="left:603px;top:1589px;width:130px;height:39px">Get Started</div>
</section>

<section class="band services" style="top:1678px;height:748px;background:var(--tint)">
  <span class="eyebrow" style="left:0;width:1200px;text-align:center;top:61px">Services</span>
  <h2 class="heading" style="left:0;width:1200px;text-align:center;top:86px">Our <b>Expertise</b></h2>

  <div class="cell" style="left:57px;top:143px;width:203px;height:257px;border-right-width:1px;border-bottom-width:1px">
    <div class="art art-blue" role="img" aria-label="Illustration of a sales trainer on a laptop screen" style="top:33px;height:138px"></div>
    <div class="cell-label" style="top:199px">Sales Training</div>
  </div>
  <div class="cell" style="left:260px;top:143px;width:226px;height:257px;border-right-width:1px;border-bottom-width:1px">
    <div class="art art-blue" role="img" aria-label="Illustration of a speaker presenting charts to an audience" style="top:33px;height:138px"></div>
    <div class="cell-label" style="top:199px">Presentation Skills<br>Training</div>
  </div>
  <div class="cell" style="left:486px;top:143px;width:228px;height:257px;border-right-width:1px;border-bottom-width:1px">
    <div class="art art-blue" role="img" aria-label="Illustration of people in a video conversation" style="top:33px;height:138px"></div>
    <div class="cell-label" style="top:199px">Stage Talks</div>
  </div>
  <div class="cell" style="left:714px;top:143px;width:231px;height:257px;border-right-width:1px;border-bottom-width:1px">
    <div class="art art-blue" role="img" aria-label="Illustration of a quick pitch beside a bar chart" style="top:33px;height:138px"></div>
    <div class="cell-label" style="top:199px">Elevator Pitches</div>
  </div>
  <div class="cell" style="left:945px;top:143px;width:201px;height:257px;border-bottom-width:1px">
    <div class="art art-blue" role="img" aria-label="Illustration of a speaker at a podium" style="top:33px;height:138px"></div>
    <div class="cell-label" style="top:199px">Keynote Speeches</div>
  </div>

  <div class="cell" style="left:57px;top:400px;width:203px;height:312px;border-right-width:1px">
    <div class="art art-blue" role="img" aria-label="Illustration of a megaphone coming out of a phone" style="top:60px;height:162px"></div>
    <div class="cell-label" style="top:250px">Marketing Collateral</div>
  </div>
  <div class="cell" style="left:260px;top:400px;width:226px;height:312px;border-right-width:1px">
    <div class="art art-blue" role="img" aria-label="Illustration of a person working on presentation slides" style="top:60px;height:162px"></div>
    <div class="cell-label" style="top:250px">Business Presentations<br>&amp; Decks</div>
  </div>
  <div class="cell" style="left:486px;top:400px;width:228px;height:312px;border-right-width:1px">
    <div class="art art-blue" role="img" aria-label="Illustration of a founder preparing an investor deck" style="top:60px;height:162px"></div>
    <div class="cell-label" style="top:250px">Venture Capital<br>Presentations &amp; Decks</div>
  </div>
  <div class="cell" style="left:714px;top:400px;width:231px;height:312px;border-right-width:1px">
    <div class="art art-blue" role="img" aria-label="Illustration of people chatting at a trade show" style="top:60px;height:162px"></div>
    <div class="cell-label" style="top:250px">Convention &amp; Trade<br>Show Messaging</div>
  </div>
  <div class="cell" style="left:945px;top:400px;width:201px;height:312px">
    <div class="art art-blue" role="img" aria-label="Illustration of people messaging through a phone" style="top:60px;height:162px"></div>
    <div class="cell-label" style="top:250px">Corporate &amp; Website<br>Messaging</div>
  </div>
</section>

<section class="results">
  <span class="eyebrow" style="left:159px;top:2504px">Achieve your goal with us</span>
  <h2 class="heading" style="left:159px;top:2531px">We are know <b>for our results</b></h2>
  <p class="copy" style="left:159px;top:2599px;width:420px">Whatever the message, and whatever the medium, we help clients establish a connection, make an impression, and drive audiences toward a predetermined course of action. This results in clear messaging, captivated audiences, and increased sales.</p>
  <div class="btn btn-fill" style="left:159px;top:2724px;width:131px;height:39px">Learn More</div>
  <div class="art art-soft" role="img" aria-label="Illustration of a man climbing steps toward a flag" style="left:630px;top:2480px;width:427px;height:325px"></div>
</section>

<section class="band testimonials" style="top:2820px;height:835px;background:var(--tint)">
  <span class="eyebrow" style="left:0;width:1200px;text-align:center;top:46px">Testimonials</span>
  <h2 class="heading" style="left:0;width:1200px;text-align:center;top:70px">Our <b>Expertise</b></h2>
  <div class="art art-soft" role="img" aria-label="Illustration of a woman on a laptop beside star rating cards" style="left:49px;top:156px;width:520px;height:512px"></div>

  <div class="quote" style="left:590px;top:123px;width:233px;min-height:203px;padding-top:50px;padding-bottom:16px">
    <span class="quote-mark" aria-hidden="true">”</span>
    <p>Hi Ellis - I love the direction and the changes you made to our marketing materials!</p>
    <h4>Daniel R.</h4>
    <small>CEO Screenline Weekly,<br>President Brightwire Media</small>
  </div>
  <div class="quote" style="left:849px;top:160px;width:232px;min-height:259px;padding-top:54px;padding-bottom:16px">
    <span class="quote-mark" aria-hidden="true">”</span>
    <p>Thank you, Ellis! I'll likely make adjustments to ensure the key operational details jump out, but I think you nailed the messaging - much more excitement and energy.</p>
    <h4 style="margin-top:12px">Nora Bellamy</h4>
    <small>Analyst, Wordloop</small>
  </div>
  <div class="quote" style="left:590px;top:391px;width:233px;min-height:260px;padding-top:50px;padding-bottom:16px">
    <span class="quote-mark" aria-hidden="true">”</span>
    <p>Ellis - Thanks a lot for your input and advice. Your suggestions will make a material difference in how I structure and present my information.</p>
    <h4>Owen T.</h4>
    <small>Chief Investment Officer,<br>Kestrel Value Partners</small>
  </div>
  <div class="quote" style="left:849px;top:448px;width:232px;min-height:244px;padding-top:54px;padding-bottom:16px">
    <span class="quote-mark" aria-hidden="true">”</span>
    <p>Dear Ellis - Thank you for your input! I truly appreciated your tips - frankly, it blew my mind (in a good way). I'm still thinking about our conversation.</p>
    <h4 style="margin-top:12px">Priya L.</h4>
    <small>Marketing Director,<br>Indigo Stage</small>
  </div>
</section>

<footer>
  <div class="band footer"></div>

  <section class="abs community">
    <h2 class="abs" style="left:29px;top:56px;font-size:30px;font-weight:300;white-space:nowrap">Join Our <b style="font-weight:700">Community!</b></h2>
    <p class="abs" style="left:29px;top:103px;width:460px;font-size:12px;line-height:19px">Ut enim ad minim veniam, quis nostrud exercitation ullamco laboris nisi ut aliquip ex ea commodo consequat aute irure.</p>
    <div class="field" style="left:29px;width:176px">Name</div>
    <div class="field" style="left:224px;width:176px">Email</div>
    <div class="btn" style="left:411px;top:152px;width:114px;height:40px;background:var(--darker);color:var(--white);font-weight:700">SUBMIT</div>
    <div class="art" role="img" aria-label="Illustration of a man with a megaphone on a laptop screen with envelopes" style="left:548px;top:9px;width:260px;height:219px;background:linear-gradient(135deg,#e8f4fd 0%,#9fd5f6 60%,#3aaeea 100%)"></div>
  </section>

  <div class="abs" style="left:177px;top:3893px;color:#e6e7ea;font-size:21px;line-height:24px;font-weight:300">MARBLE<br>FINCH CO</div>
  <p class="ft" style="left:169px;top:3964px;width:250px;line-height:19px">Ut enim ad minim veniam, quis nostrud exercitation ullamco laboris nisi ut aliquip ex ea commodo consequat aute irure.</p>
  <svg class="abs" style="left:168px;top:4045px" width="180" height="14" aria-label="Social links">
    <circle cx="6" cy="7" r="5" fill="#fff"/><circle cx="45" cy="7" r="5" fill="#fff"/><circle cx="84" cy="7" r="5" fill="#fff"/><circle cx="123" cy="7" r="5" fill="#fff"/><circle cx="162" cy="7" r="5" fill="#fff"/>
  </svg>

  <h3 class="ft-h" style="left:553px;top:3906px">Quick Links</h3>
  <div class="ft" style="left:553px;top:3948px">Home<br>FinchCamp<br>Testimonials<br>Team<br>Contact</div>

  <h3 class="ft-h" style="left:811px;top:3906px">Contact Us</h3>
  <svg class="abs" style="left:813px;top:3955px" width="12" height="16" aria-hidden="true"><path d="M6 1a5 5 0 0 1 5 5c0 4-5 9-5 9S1 10 1 6a5 5 0 0 1 5-5z" fill="#fff"/><circle cx="6" cy="6" r="2" fill="#1c1c1f"/></svg>
  <div class="ft" style="left:842px;top:3952px;line-height:19px">14 Larkspur Lane,<br>Eastbrook,<br>CT 06100</div>
  <svg class="abs" style="left:813px;top:4026px" width="13" height="13" aria-hidden="true"><path d="M3 1l2.5 3-1.5 1.5a8 8 0 0 0 3.5 3.5L9 7.5l3 2.5-1.5 2.5C5 12 1 8 .5 2.5z" fill="#fff"/></svg>
  <div class="ft" style="left:842px;top:4018px">(555) 010-2040</div>
  <svg class="abs" style="left:813px;top:4060px" width="14" height="11" aria-hidden="true"><rect x=".5" y=".5" width="13" height="10" fill="none" stroke="#fff"/><path d="M.5 .5l6.5 6 6.5-6" fill="none" stroke="#fff"/></svg>
  <div class="ft" style="left:842px;top:4052px">hello@marblefinchco.com</div>

  <div class="band footer-bar"></div>
  <div class="ft" style="left:159px;top:4140px;font-size:11px">Copyright ©MarbleFinchCo. All rights reserved.</div>
  <div class="ft" style="left:821px;top:4140px;font-size:11px">Privacy Policy &nbsp;&nbsp;&nbsp;|&nbsp;&nbsp;&nbsp; Terms of conditions</div>
</footer>

</body>
</html>
```